I have a requirement for a simple website that I can manage and change content myself. I'd like to be able to include and change images frequently.

I run a small consulting firm and focus on the area of small to medium sized business turn around. The premise of the business service is that most small businesses "have a monkey on their back" - a problem they need to solve - for example "a Sales Monkey" where their sales team didn't have a solid process or approach or training or the right people; or "a Finance Monkey" where they needed help with Cash flow management or funding, or "an IT Monkey" where their IT systems aren't supporting their supply chain process or ordering process.

So the whole business is build around building monkey characters to represent specific business problems - thus the name Quiet Harbour Partners.

This always builds into giving each employee their own Monkey character - mine is an Orangutan and appears on my card and Derek (who is our Lawyer) is a Baboon and his character is on his card. I'd like to see these characters also integrated into the site.

The site need to be pretty simple at this stage:

1. Home Page
2. Services Page
3. Who we are / team page
4. Contact Us page

Due to the nature of the name and the imagery around the business I'd like the site to be engaging and colourful, the language I'll use is accessible, down to earth and customer/solution focused.

Target Market(s)

Small to medium sized enterprises looking for assistance with their business. They will be looking for practical solutions at value for money pricing

Industry/Entity Type

Business Service

Requirements
Nice to have
• I'd like the monkey in the logo to swing.

On the People or team page - each person is to have their own monkey character - for example - my business card shows my monkey character as an Orangutan and Derek's monkey character is a baboon - so as the business grows each new person gets their own monkeys character. So on the people or team page it would be fun to have some kind of jungle scene with the character monkeys placed in there and some descriptor of the person.

```html
<!DOCTYPE html>
<html lang="en">
<head>
<meta charset="utf-8">
<title>Quiet Harbour Partners – Services</title>
<link href="https://fonts.googleapis.com/css2?family=Titillium+Web:wght@400;600&family=Nunito:wght@600;700&family=Roboto+Slab:wght@600&display=swap" rel="stylesheet">
<style>
  :root{
    --yellow:#dcc500;
    --yellow-dark:#c9b000;
    --yellow-soft:#e6d54a;
    --brown:#6b4a12;
    --brown-text:#5a4a1a;
    --ink:#3d3d3d;
    --body:#4a4a4a;
    --page:#e9e9e9;
    --white:#ffffff;
  }
  *{box-sizing:border-box;margin:0;padding:0}
  html,body{width:1034px;height:1200px;overflow:hidden}
  body{
    background:var(--page);
    font-family:"Titillium Web",sans-serif;
    color:var(--body);
    position:relative;
  }
  .masthead{
    position:absolute;left:0;top:0;width:1034px;height:301px;
    background:var(--yellow-dark);
  }
  .masthead-panel{
    position:absolute;left:69px;top:14px;width:896px;height:287px;
    background:var(--yellow);
  }
  .gear-art{
    position:absolute;left:494px;top:14px;width:352px;height:273px;
    background:radial-gradient(circle at 45% 50%, rgba(240,226,110,.75) 0%, rgba(240,226,110,.45) 45%, rgba(220,197,0,0) 72%);
  }
  .topbar{
    position:absolute;left:122px;top:36px;width:789px;height:56px;
    background:var(--white);
    border-bottom:3px solid var(--yellow-dark);
    display:flex;align-items:center;
  }
  .brand{
    width:265px;padding-left:14px;
    font-family:"Titillium Web",sans-serif;font-weight:400;font-size:19px;
    color:var(--brown);letter-spacing:.3px;
  }
  .nav{display:flex;height:100%}
  .nav a{
    display:flex;align-items:center;justify-content:center;height:100%;
    border-left:1px solid #e6e6e6;
    font-size:12px;color:var(--ink);text-decoration:none;
  }
  .nav a.current{font-weight:600;color:var(--brown)}
  .nav .home{width:70px}
  .nav .services{width:77px}
  .nav .team{width:157px}
  .nav .contact{width:89px}
  .social{
    display:flex;gap:14px;align-items:center;justify-content:center;
    height:100%;width:131px;border-left:1px solid #e6e6e6;
  }
  .social span{display:block;width:18px;height:18px;border-radius:50%;background:var(--brown)}
  .hero-title{
    position:absolute;left:144px;top:166px;
    font-family:"Nunito",sans-serif;font-weight:700;font-size:30px;color:var(--brown-text);
    line-height:1;
  }
  .hero-sub{
    position:absolute;left:144px;top:198px;
    font-family:"Nunito",sans-serif;font-weight:600;font-size:15px;color:var(--brown-text);
  }
  .content{
    position:absolute;left:69px;top:301px;width:896px;height:867px;background:var(--white);
  }
  .intro{position:absolute;left:27px;top:24px;width:845px}
  .intro h2{font-family:"Nunito",sans-serif;font-weight:700;font-size:18px;color:var(--ink);margin-bottom:13px}
  .intro p{font-size:10.3px;line-height:14.8px;margin-bottom:14.8px}
  .service{position:absolute;left:0;width:896px;height:200px}
  .ribbon{position:absolute;left:0;top:0;width:364px;height:60px}
  .ribbon-title{
    position:absolute;left:157px;top:6px;
    font-family:"Roboto Slab",serif;font-weight:600;font-size:19px;color:var(--white);line-height:1;
  }
  .ribbon-tag{
    position:absolute;left:159px;top:28px;
    font-family:"Roboto Slab",serif;font-weight:600;font-size:13px;color:var(--white);line-height:1;
  }
  .character{position:absolute;left:20px;top:16px;width:148px;height:126px;border-radius:40px 40px 20px 20px}
  .character.chimp{background:linear-gradient(160deg,#5a4a3c,#c9a27a)}
  .character.macaque{background:linear-gradient(160deg,#e8b7a0,#cdb89a)}
  .character.proboscis{background:linear-gradient(160deg,#e7a040,#dfe0d2)}
  .service-body{position:absolute;left:180px;top:64px;width:686px}
  .service-body h3{font-family:"Nunito",sans-serif;font-weight:700;font-size:15.5px;color:var(--ink);margin-bottom:9px}
  .service-body p{font-size:10.3px;line-height:14.8px;margin-bottom:14.8px;padding-left:2px}
  .footer{position:absolute;left:0;top:1175px;width:1034px;text-align:center;font-size:10.5px;color:var(--ink)}
</style>
</head>
<body>
  <header class="masthead">
    <div class="masthead-panel"></div>
    <div class="gear-art" role="img" aria-label="Large faint cog decoration"></div>
    <div class="topbar">
      <div class="brand">Quiet Harbour Partners</div>
      <nav class="nav">
        <a class="home" href="#">Home</a>
        <a class="services current" href="#">Services</a>
        <a class="team" href="#">Who we are / team page</a>
        <a class="contact" href="#">Contact Us</a>
      </nav>
      <div class="social" aria-label="Social links">
        <span></span><span></span><span></span>
      </div>
    </div>
    <h1 class="hero-title">Overview of Our Services</h1>
    <p class="hero-sub">We can create high impact on your business with limited budget</p>
  </header>

  <main class="content">
    <section class="intro">
      <h2>Get introduced to our services</h2>
      <p>Lorem ipsum dolor sit amet, consectetuer adipiscing elit, sed diam nonummy nibh euismod tincidunt ut laoreet dolore magna aliquam erat volutpat. Ut wisi enim ad minim veniam, quis nostrud exerci tation ullamcorper suscipit lobortis nisl</p>
      <p>ut aliquip ex ea commodo consequat. Duis autem vel eum iriure dolor in hendrerit in vulputate velit esse molestie consequat, vel illum dolore eu feugiat nulla facilisis at vero eros et accumsan</p>
    </section>

    <section class="service" style="top:177px">
      <svg class="ribbon" viewBox="0 0 364 60" aria-hidden="true">
        <path d="M0 0H364V22L318 51H0Z" fill="#dcc500"/>
        <path d="M364 22Q356 44 318 51Q344 40 352 20Z" fill="#efe39a"/>
      </svg>
      <div class="character chimp" role="img" aria-label="Sales and marketing monkey character"></div>
      <div class="ribbon-title">Sales/Marketing</div>
      <div class="ribbon-tag">Monkey</div>
      <div class="service-body">
        <h3>Ut wisi enim ad minim veniam</h3>
        <p>quis nostrud exerci tation ullamcorper suscipit lobortis nisl ut aliquip ex ea commodo consequat. Duis autem vel eum iriure dolor in hendrerit in vulputate velit esse molestie consequat, vel illum dolore eu feugiat nulla facilisis at vero eros et accumsan et iusto odio dignissim qui blandit praesent luptatum zzril delenit augue duis dolore te feugait nulla facilisi. Nam liber tempor cum soluta nobis eleifend ...</p>
        <p>Ut wisi enim ad minim veniam, quis nostrud exerci tation ullamcorper suscipit lobortis nisl ut aliquip ex ea commodo consequat. Duis autem vel eum iriure dolor in hendrerit in vulputate velit esse molestie consequat,</p>
      </div>
    </section>

    <section class="service" style="top:410px">
      <svg class="ribbon" viewBox="0 0 364 60" aria-hidden="true">
        <path d="M0 0H364V22L318 51H0Z" fill="#dcc500"/>
        <path d="M364 22Q356 44 318 51Q344 40 352 20Z" fill="#efe39a"/>
      </svg>
      <div class="character macaque" role="img" aria-label="Business process monkey character"></div>
      <div class="ribbon-title">Business Process</div>
      <div class="ribbon-tag">Monkey</div>
      <div class="service-body">
        <h3>Ut wisi enim ad minim veniam</h3>
        <p>quis nostrud exerci tation ullamcorper suscipit lobortis nisl ut aliquip ex ea commodo consequat. Duis autem vel eum iriure dolor in hendrerit in vulputate velit esse molestie consequat, vel illum dolore eu feugiat nulla facilisis at vero eros et accumsan et iusto odio dignissim qui blandit praesent luptatum zzril delenit augue duis dolore te feugait nulla facilisi. Nam liber tempor cum soluta nobis eleifend ...</p>
        <p>Ut wisi enim ad minim veniam, quis nostrud exerci tation ullamcorper suscipit lobortis nisl ut aliquip ex ea commodo consequat. Duis autem vel eum iriure dolor in hendrerit in vulputate velit esse molestie consequat,</p>
      </div>
    </section>

    <section class="service" style="top:640px">
      <svg class="ribbon" viewBox="0 0 364 60" aria-hidden="true">
        <path d="M0 0H364V22L318 51H0Z" fill="#dcc500"/>
        <path d="M364 22Q356 44 318 51Q344 40 352 20Z" fill="#efe39a"/>
      </svg>
      <div class="character proboscis" role="img" aria-label="Finance and IT monkey character"></div>
      <div class="ribbon-title">Finance and IT</div>
      <div class="ribbon-tag">Monkey</div>
      <div class="service-body">
        <h3>Ut wisi enim ad minim veniam</h3>
        <p>quis nostrud exerci tation ullamcorper suscipit lobortis nisl ut aliquip ex ea commodo consequat. Duis autem vel eum iriure dolor in hendrerit in vulputate velit esse molestie consequat, vel illum dolore eu feugiat nulla facilisis at vero eros et accumsan et iusto odio dignissim qui blandit praesent luptatum zzril delenit augue duis dolore te feugait nulla facilisi. Nam liber tempor cum soluta nobis eleifend ...</p>
        <p>Ut wisi enim ad minim veniam, quis nostrud exerci tation ullamcorper suscipit lobortis nisl ut aliquip ex ea commodo consequat. Duis autem vel eum iriure dolor in hendrerit in vulputate velit esse molestie consequat,</p>
      </div>
    </section>
  </main>

  <footer class="footer">Copyright © 2013 Quiet Harbour Partners.</footer>
</body>
</html>
```